Business Cards for an 'affordable luxury' inner city home builder in Calgary.

We need a business card design that emulates the progressive, innovative, culture of our company and the modern style of our homes. Use our website www.velmarcrest-ab.com as a reference for the product we build.

Our company builds homes in the inner city space of Calgary, Alberta. We build affordable luxury.

Target Market(s)

Young professional Families

Contact Information for Business Card

Try to maintain consistency with the logo font and the card font.

Requirements
Must have
• The details must include: Name, education, title, phone number, website and email (Address is not as important)
• The design must be uniques (like our logo), elegant, sophisticated and modern.

```html
<!DOCTYPE html>
<html lang="en">
<head>
<meta charset="utf-8">
<title>Velmarcrest Homes Ltd – Business Card</title>
<link href="https://fonts.googleapis.com/css2?family=Lato:wght@400;700&display=swap" rel="stylesheet">
<style>
  :root{
    --bg:#5c5c5c;
    --card-dark:#222222;
    --card-light:#ffffff;
    --panel-grey-light:#8c8c8c;
    --panel-grey-dark:#6f6f6f;
    --faint-grey:#f1f1f1;
    --text-light:#ffffff;
    --text-dark:#1e1e1e;
  }
  *{margin:0;padding:0;box-sizing:border-box}
  html,body{width:1200px;height:802px;overflow:hidden}
  body{background:var(--bg);font-family:"Lato",sans-serif;position:relative}

  .card{position:absolute;top:274px;width:442px;height:264px;box-shadow:0 3px 8px rgba(0,0,0,.45);overflow:hidden}
  .card--back{left:136px;background:var(--card-dark);color:var(--text-light)}
  .card--front{left:624px;background:var(--card-light);color:var(--text-dark)}

  .card__artwork{position:absolute;left:0;top:0;width:238px;height:264px}

  .person{position:absolute;right:22px;top:70px;text-align:right}
  .person__name{font-weight:700;font-size:17px;letter-spacing:.2px;line-height:1}
  .person__title{font-size:12.5px;line-height:1;margin-top:3px}
  .person__education{font-size:11px;line-height:1;margin-top:4px;opacity:.85}

  .contacts{position:absolute;right:22px;top:136px;list-style:none;text-align:right;font-size:12.5px;line-height:16.5px}
  .contacts li{display:flex;justify-content:flex-end;align-items:center;gap:3px}
  .contacts svg{width:9px;height:9px;fill:var(--text-light)}

  .card__watermark{position:absolute;left:0;top:0;width:210px;height:264px}

  .brand{position:absolute;left:100px;top:107px;display:flex;align-items:center;gap:22px}
  .brand__mark{width:46px;height:46px;background:var(--text-dark)}
  .brand__name{font-weight:700;font-size:22px;letter-spacing:1.4px;line-height:24px}
</style>
</head>
<body>
  <section class="card card--back">
    <svg class="card__artwork" viewBox="0 0 238 264" role="img" aria-label="Large grey architectural building symbol of the company">
      <defs>
        <linearGradient id="artworkTone" x1="0" y1="0" x2="1" y2="1">
          <stop offset="0" stop-color="#8c8c8c"/>
          <stop offset="1" stop-color="#6f6f6f"/>
        </linearGradient>
      </defs>
      <polygon points="0,0 154,0 154,200 238,250 238,264 0,264" fill="url(#artworkTone)"/>
    </svg>
    <div class="person">
      <p class="person__name">DANIEL HARROW</p>
      <p class="person__title">Managing Director</p>
      <p class="person__education">B.Sc. Civil Engineering</p>
    </div>
    <ul class="contacts">
      <li>044-987 654 321
        <svg viewBox="0 0 10 10"><path d="M1 3c0-1.5 8-1.5 8 0v1H7V3H3v1H1zM2 5h6l1 4H1z"/></svg></li>
      <li>info@velmarcrest-ab.com
        <svg viewBox="0 0 10 10"><rect x="0" y="2" width="10" height="7"/></svg></li>
      <li>www.velmarcrest-ab.com
        <svg viewBox="0 0 10 10"><circle cx="5" cy="5" r="5"/></svg></li>
    </ul>
  </section>

  <section class="card card--front">
    <svg class="card__watermark" viewBox="0 0 210 264" role="img" aria-label="Faint large building symbol in the background">
      <defs>
        <linearGradient id="watermarkTone" x1="0" y1="0" x2="1" y2="0">
          <stop offset="0" stop-color="#efefef"/>
          <stop offset="1" stop-color="#ffffff"/>
        </linearGradient>
      </defs>
      <rect width="210" height="264" fill="url(#watermarkTone)"/>
    </svg>
    <div class="brand">
      <span class="brand__mark"></span>
      <p class="brand__name">VELMARCREST<br>HOMES LTD</p>
    </div>
  </section>
</body>
</html>
```